Experienced Home remodel service

I'm a home remodeler. I want a catch phrase that clearly describes viewers what kind of work I'm in like the purple phrase on my rough draft idea. I need my website, phone, logo, slogan included. The picture is of my daughter. I want her on it. Be cool if something could be added to her picture like a hard hat or tool belt ect and her picture cut out/background removed. Some kind of background other than plain white for whole picture. I added extra pics of her so pick one

Target Market(s)

Home owners between 30-60

Industry/Entity Type

Home renovation/remodel

Colors

Designer to choose colors to be used in the design.

Requirements
Must have
• Daughters picture incorporated. Logo, phone, website address, slogan,
Nice to have
• See a hardhat or tool belt added to one of my daughters pictures that is chosen to use by designer

```html
<!DOCTYPE html>
<html lang="en">
<head>
<meta charset="utf-8">
<title>Harlow Home Solutions – Yard Sign</title>
<link href="https://fonts.googleapis.com/css2?family=Bebas+Neue&family=Poppins:wght@400;700;800&display=swap" rel="stylesheet">
<style>
  :root {
    --page: #b0b0b0;
    --ink: #111111;
    --black: #000000;
    --white: #ffffff;
    --band-grey: #c8c8c8;
    --rule: #9a9a9a;
    --photo-top: #f2d8ef;
    --photo-bottom: #c9a6d8;
  }
  html, body {
    margin: 0;
    width: 1200px;
    height: 847px;
    overflow: hidden;
    background: var(--page);
  }
  .sign {
    position: absolute;
    left: 20px;
    top: 135px;
    width: 1160px;
    height: 576px;
    background: var(--white);
    overflow: hidden;
  }
  .header-band {
    position: absolute; left: 0; top: 0;
    width: 100%; height: 307px;
    background: var(--black);
  }
  .slogan-band {
    position: absolute; left: 0; top: 307px;
    width: 100%; height: 74px;
    background: var(--band-grey);
  }
  .brand-name {
    position: absolute; left: 68px; top: 42px;
    margin: 0; color: var(--white); line-height: 1;
  }
  .brand-name__top {
    display: block;
    font-family: "Bebas Neue", sans-serif;
    font-size: 150px;
    letter-spacing: 1px;
    white-space: nowrap;
  }
  .brand-name__bottom {
    display: block;
    margin-top: -18px;
    font-family: "Poppins", sans-serif;
    font-weight: 400;
    font-size: 124px;
    letter-spacing: -2px;
    white-space: nowrap;
  }
  .services {
    position: absolute; left: 844px; top: 44px;
    width: 249px; margin: 0; padding: 0; list-style: none;
  }
  .services__item {
    display: flex; align-items: center;
    height: 76px;
    border-bottom: 2px dotted rgba(255,255,255,0.8);
  }
  .services__item:last-child { border-bottom: none; }
  .services__icon { width: 40px; height: 40px; flex: none; }
  .services__label {
    margin-left: 57px;
    font-family: "Bebas Neue", sans-serif;
    font-size: 57px;
    line-height: 1;
    color: var(--white);
    padding-top: 6px;
  }
  .slogan {
    position: absolute; left: 68px; top: 307px;
    height: 74px; line-height: 76px; margin: 0;
    font-family: "Poppins", sans-serif;
    font-weight: 800; font-size: 46px; letter-spacing: -1px;
    color: var(--ink); white-space: nowrap;
  }
  .phone {
    position: absolute; left: 64px; top: 390px; margin: 0;
    font-family: "Poppins", sans-serif;
    font-weight: 800; font-size: 98px; letter-spacing: -4px;
    line-height: 1.1; color: var(--ink); white-space: nowrap;
  }
  .website {
    position: absolute; left: 68px; top: 498px; margin: 0;
    font-family: "Poppins", sans-serif;
    font-weight: 700; font-size: 32px; letter-spacing: 2px;
    color: var(--ink); white-space: nowrap;
  }
  .divider {
    position: absolute; left: 733px; top: 406px;
    width: 2px; height: 127px; background: var(--rule);
  }
  .logo-lockup {
    position: absolute; left: 748px; top: 440px; width: 156px;
    text-align: center; font-family: "Poppins", sans-serif; color: var(--ink);
  }
  .logo-lockup__mark {
    display: block; width: 26px; height: 26px;
    margin: 0 auto 10px; background: var(--ink);
  }
  .logo-lockup__name {
    font-weight: 800; font-size: 10.5px; letter-spacing: 1px; line-height: 1.05;
  }
  .logo-lockup__tag {
    margin-top: 6px; font-weight: 400; font-size: 7px; letter-spacing: 1.6px; line-height: 1.2;
  }
  .portrait {
    position: absolute; left: 905px; top: 271px;
    width: 220px; height: 305px;
    border-radius: 110px 110px 0 0;
    background: linear-gradient(180deg, var(--photo-top), var(--photo-bottom));
  }
</style>
</head>
<body>
  <main class="sign">
    <div class="header-band"></div>
    <div class="slogan-band"></div>

    <h1 class="brand-name">
      <span class="brand-name__top">HARLOW HOME</span>
      <span class="brand-name__bottom">SOLUTIONS</span>
    </h1>

    <ul class="services">
      <li class="services__item">
        <svg class="services__icon" viewBox="0 0 40 40" aria-hidden="true">
          <path d="M20 4 L38 20 L34 20 L34 36 L6 36 L6 20 L2 20 Z" fill="#fff"/>
          <rect x="16" y="24" width="8" height="12" fill="#000"/>
        </svg>
        <span class="services__label">BUILD</span>
      </li>
      <li class="services__item">
        <svg class="services__icon" viewBox="0 0 40 40" aria-hidden="true">
          <path d="M6 34 L30 10" stroke="#fff" stroke-width="6" stroke-linecap="round"/>
          <circle cx="31" cy="9" r="6" fill="none" stroke="#fff" stroke-width="4"/>
          <path d="M8 6 L34 32" stroke="#fff" stroke-width="5" stroke-linecap="round"/>
        </svg>
        <span class="services__label">REPAIR</span>
      </li>
      <li class="services__item">
        <svg class="services__icon" viewBox="0 0 40 40" aria-hidden="true">
          <rect x="22" y="4" width="16" height="12" rx="2" fill="#fff"/>
          <rect x="2" y="24" width="16" height="12" rx="2" fill="#fff"/>
          <path d="M16 8 H8 V18 M5 15 L8 19 L11 15" stroke="#fff" stroke-width="3" fill="none"/>
          <path d="M24 32 H32 V22 M29 25 L32 21 L35 25" stroke="#fff" stroke-width="3" fill="none"/>
        </svg>
        <span class="services__label">REPLACE</span>
      </li>
    </ul>

    <p class="slogan">FOR ALL YOUR HOME REMODEL NEEDS</p>

    <p class="phone">555-214-3870</p>
    <p class="website">www.harlowhomesolutions.com</p>

    <div class="divider"></div>

    <div class="logo-lockup">
      <span class="logo-lockup__mark"></span>
      <div class="logo-lockup__name">HARLOW HOME<br>SOLUTIONS</div>
      <div class="logo-lockup__tag">BUILD. REPAIR. REPLACE.<br>(555) 214 3870</div>
    </div>

    <div class="portrait" role="img" aria-label="Cut-out photo of the owner's young daughter smiling in a yellow hard hat, lilac jacket and tool belt, holding a hammer"></div>
  </main>
</body>
</html>
```